Halbrecht Ferrant Long Wheel Base 2020 - Car Wrap for a carpet store

Carpet store selling as well online a s in the showroom, shop. High quality rugs, middle to high end of the market, we want to promote as well lindorvelt.be and Vermaro, as our 2 brands. Use photos from Lindorvelt.be or Vermaro. We want something classy, clean, using some big interior shots and clever placed text: the web addresses, shop address, Belgian family business since 1907

Target Market(s)

middle -> high end

Industry/Entity Type

Interior design , rugs and carpets

Font styles to use
Serif

Colors

Designer to choose colors to be used in the design.

Requirements
Must have
• interior shots, text: the web addresses, shop address, Belgian family business since 1907

```html
<!DOCTYPE html>
<html lang="en">
<head>
<meta charset="utf-8">
<title>Lindorvelt – van wrap</title>
<link rel="stylesheet" href="https://fonts.googleapis.com/css2?family=Jost:wght@400&family=Poppins:wght@400;600&display=swap">
<style>
  :root{
    --brand-blue:#1f73b7;
    --body-white:#f7f7f6;
    --page:#f1f2f3;
    --trim:#262829;
    --glass:#8b9095;
    --tyre:#1d1e1f;
    --rim:#c9cbcd;
    --photo-warm:#b9a98e;
    --photo-cool:#9aa4ad;
  }
  html,body{margin:0;padding:0;width:1200px;height:1200px;overflow:hidden;background:var(--page);}
  .wrap-sheet{display:block;width:1200px;height:1200px;}
  .brand-name{font-family:"Jost",sans-serif;font-weight:400;fill:var(--brand-blue);}
  .web{font-family:"Poppins",sans-serif;font-weight:400;}
  .phone,.since{font-family:"Poppins",sans-serif;font-weight:600;}
  .address{font-family:"Poppins",sans-serif;font-weight:400;}
  .on-blue{fill:#fff;}
  .on-white{fill:var(--brand-blue);}
</style>
</head>
<body>
<svg class="wrap-sheet" viewBox="0 0 960 960" xmlns="http://www.w3.org/2000/svg">
  <defs>
    <clipPath id="body-top">
      <path d="M160 362 L163 205 Q165 170 195 166 L530 164 Q600 166 640 176 Q680 190 712 225 L760 262 Q790 272 798 292 L800 362 Z"/>
    </clipPath>
    <clipPath id="body-bottom">
      <path d="M160 732 L163 575 Q165 540 195 536 L530 534 Q600 536 640 546 Q680 560 712 595 L760 632 Q790 642 798 662 L800 732 Z"/>
    </clipPath>
    <linearGradient id="interior-tones" x1="0" y1="0" x2="1" y2="1">
      <stop offset="0" stop-color="var(--photo-warm)"/>
      <stop offset=".55" stop-color="#d9d6cf"/>
      <stop offset="1" stop-color="var(--photo-cool)"/>
    </linearGradient>
  </defs>

  <g class="van van-side-a">
    <g clip-path="url(#body-top)">
      <rect x="150" y="150" width="660" height="220" fill="var(--body-white)"/>
      <path d="M445 160 L820 160 L820 370 L430 370 Q520 350 535 265 Q530 190 445 160 Z" fill="var(--brand-blue)"/>
      <path d="M538 178 L628 178 Q660 196 670 228 L668 252 L538 252 Z" fill="var(--glass)"/>
      <rect x="150" y="332" width="660" height="40" fill="var(--trim)"/>
      <path d="M745 275 L800 285 L800 300 L750 300 Z" fill="var(--trim)"/>
      <rect x="172" y="265" width="10" height="35" fill="#b42a2a"/>
    </g>
    <text class="brand-name" x="196" y="248" font-size="46">lindorvelt</text>
    <rect x="185" y="276" width="180" height="24" fill="var(--brand-blue)"/>
    <text class="web on-blue" x="198" y="293" font-size="12">www.<tspan font-weight="600">lindorvelt</tspan>.be</text>
    <text class="phone on-blue" x="547" y="298" font-size="12">+32 (0) 3 71 540 29</text>
    <text class="since on-blue" x="680" y="298" font-size="9.5">since 1907</text>
    <text class="address on-blue" x="548" y="328" font-size="5.6">Brouwerslaan 27,</text>
    <text class="address on-blue" x="548" y="336" font-size="5.6">2830 Veldemond, Belgium</text>
    <g class="wheel"><circle cx="272" cy="360" r="44" fill="var(--trim)"/><circle cx="272" cy="360" r="36" fill="var(--tyre)"/><circle cx="272" cy="360" r="22" fill="var(--rim)"/></g>
    <g class="wheel"><circle cx="700" cy="360" r="44" fill="var(--trim)"/><circle cx="700" cy="360" r="36" fill="var(--tyre)"/><circle cx="700" cy="360" r="22" fill="var(--rim)"/></g>
  </g>

  <g class="van van-side-b">
    <g clip-path="url(#body-bottom)">
      <rect x="150" y="520" width="660" height="220" fill="var(--body-white)"/>
      <path d="M150 520 L245 520 Q270 600 330 650 Q360 680 390 705 L150 705 Z" fill="url(#interior-tones)" role="img" aria-label="Interior photograph of a living room with a sofa and a patterned rug"/>
      <path d="M245 520 L262 520 Q290 620 390 680 Q520 710 650 700 L820 690 L820 740 L150 740 L150 705 L390 705 Q300 640 245 520 Z" fill="var(--brand-blue)"/>
      <path d="M380 690 Q520 712 660 706" fill="none" stroke="#fff" stroke-width="2"/>
      <path d="M538 548 L628 548 Q660 566 670 598 L668 622 L538 622 Z" fill="var(--glass)"/>
      <rect x="150" y="707" width="660" height="35" fill="var(--trim)"/>
      <path d="M745 645 L800 655 L800 670 L750 670 Z" fill="var(--trim)"/>
      <rect x="172" y="635" width="10" height="35" fill="#b42a2a"/>
    </g>
    <circle cx="342" cy="602" r="20" fill="none" stroke="var(--brand-blue)" stroke-width="2.5"/>
    <text class="brand-name" x="370" y="614" font-size="39">lindorvelt</text>
    <text class="web on-white" x="381" y="664" font-size="11">www.<tspan font-weight="600">lindorvelt</tspan>.be</text>
    <text class="phone on-white" x="541" y="664" font-size="12">+32 (0) 3 71 540 29</text>
    <text class="since on-white" x="680" y="664" font-size="9.5">since 1907</text>
    <text class="address on-white" x="542" y="682" font-size="5.6">Brouwerslaan 27,</text>
    <text class="address on-white" x="542" y="690" font-size="5.6">2830 Veldemond, Belgium</text>
    <g class="wheel"><circle cx="272" cy="730" r="44" fill="var(--trim)"/><circle cx="272" cy="730" r="36" fill="var(--tyre)"/><circle cx="272" cy="730" r="22" fill="var(--rim)"/></g>
    <g class="wheel"><circle cx="700" cy="730" r="44" fill="var(--trim)"/><circle cx="700" cy="730" r="36" fill="var(--tyre)"/><circle cx="700" cy="730" r="22" fill="var(--rim)"/></g>
  </g>
</svg>
</body>
</html>
```